Trucking Insurance Website Design

We are working with a Trucking Insurance company in California. They provide vehicle insurance for trucking companies and truckers.
As you might imagine, there are no websites we could find for inspiration for trucking insurance. But below are sites that do similar insurance.
https://pinemeadowcover.com/trucking-insurance/
https://www.haulsafeplan.com/california-commercial-truck-insurance
Thank you for taking the time to consider designing a website for us. We are web developers based in Stockton, CA, USA. Most of our projects go through the same process. Understanding this process may help you win a project with us. We custom-code all of our websites in-house. We don’t have any requirements as to what tools you use for your design, but we ask that you follow these guidelines.
IMAGES:
If you use any images or icons in the design, we ask that you have a link to the asset so we can purchase the image/icon. Most of the designs we submit do not have the customer’s images on them unless they have some great images. Be creative; show us the feeling you are trying to portray with your image choices. Use any royalty-free site you choose. We subscribe to Quillon and mainly use their images, but we can purchase images outside of Quillon. PLEASE NOTE: we will not submit designs to clients with watermarks on the images.
FONTS:
We ask that you identify the fonts you’re using in the design. This can be done in a message if you want. We typically use Tavlo Fonts and Quillon Fonts.
CONTENT:
We're always open to different content and ideas. We often submit designs with stock images so the client can see our vision. We typically take pictures after the website launch to use their images with our vision. Lorem Ipsum is fine for paragraphs, but we ask that you make the Headers with correct English. We want to be able to show the vision and identify the sections of the website.
INSPIRATION:
We typically add a couple of links in the brief of websites we like to help you get started in your design.
REVISIONS:
We do not often ask for revisions of the designs unless we see something in the design that may not appeal to the client. If there are slight changes that we want to make, we do that in the development process.
FEEDBACK:
We rarely give feedback on designs during the design process. We are working on many website projects and do not have the time to provide feedback. We usually respond if your request is well thought out and asks specific questions, but a note asking “feedback, please” usually goes unanswered.
1 page

```html
<!DOCTYPE html>
<html lang="en">
<head>
<meta charset="utf-8">
<title>Ridgeline Insurance – Trucking Insurance in California</title>
<link href="https://fonts.googleapis.com/css2?family=Poppins:ital,wght@0,400;0,500;0,600;0,700;1,400&display=swap" rel="stylesheet">
<style>
:root{
  --blue:#6a7dc8;
  --red:#c1161d;
  --ink:#1f1f1f;
  --grey-band:#efefef;
  --footer:#6f6f6f;
  --topbar:#727272;
  --white:#ffffff;
}
*{margin:0;padding:0;box-sizing:border-box}
html,body{width:1200px;height:3783px;overflow:hidden}
body{position:relative;font-family:'Poppins',sans-serif;color:var(--ink);background:var(--white)}
.abs{position:absolute}
.btn{position:absolute;display:flex;align-items:center;justify-content:center;color:var(--white);font-weight:600;font-size:14px;letter-spacing:.3px;text-transform:uppercase}
.btn-red{background:var(--red)}
.btn-blue{background:var(--blue)}

/* header */
.topbar{left:570px;top:0;width:630px;height:53px;background:var(--topbar);border-bottom-left-radius:16px;display:flex;align-items:center;justify-content:flex-end;gap:30px;padding-right:73px;color:var(--white);font-weight:600;font-size:20px}
.topbar span{display:flex;align-items:center;gap:12px}
.brand{left:73px;top:18px;width:146px;text-align:center}
.brand-mark{display:block;width:40px;height:40px;border-radius:50%;background:var(--red);margin:0 auto 8px}
.brand-name{display:block;font-weight:500;font-size:12px;letter-spacing:5px;color:#333;line-height:14px}
.nav a{position:absolute;top:81px;white-space:nowrap;color:var(--ink);text-decoration:none;font-weight:600;font-size:14px}
.header-line{left:0;top:119px;width:1200px;height:1px;background:#ddd}

/* hero */
.hero{left:0;top:120px;width:1200px;height:617px;background:
  radial-gradient(ellipse 420px 260px at 330px 390px,#2f8fa6 0%,rgba(47,143,166,0) 70%),
  radial-gradient(ellipse 500px 200px at 300px 640px,#5a5550 0%,rgba(90,85,80,0) 70%),
  radial-gradient(ellipse 520px 380px at 1000px 300px,#f4d6bc 0%,rgba(244,214,188,0) 75%),
  linear-gradient(180deg,#6e9fb3 0%,#b9c7c6 45%,#9a8b7c 80%,#5b5149 100%)}
.hero-title{right:72px;top:330px;text-align:right;font-weight:600;font-size:47px;letter-spacing:.5px;line-height:56px;color:var(--ink)}
.hero-sub{right:72px;top:388px;text-align:right;font-weight:600;font-size:30px;line-height:37px}

/* welcome */
.welcome-h{left:75px;top:812px;font-weight:700;font-size:41px;line-height:48px}
.welcome-h .blue{color:var(--blue)}
.welcome-p{left:75px;top:924px;width:510px;font-size:15.3px;line-height:32.4px}
.welcome-accent{left:884px;top:812px;width:243px;height:357px;background:var(--red)}
.welcome-photo{left:623px;top:842px;width:435px;height:391px;border:4px solid var(--white);background:
  radial-gradient(ellipse 120px 60px at 55% 58%,#f2f2f2 0%,rgba(242,242,242,0) 80%),
  radial-gradient(ellipse 200px 140px at 40% 25%,#2a2a2a 0%,rgba(42,42,42,0) 80%),
  linear-gradient(180deg,#3a3a3a 0%,#4d4d4d 60%,#c9c9c9 100%)}

/* truck types */
.types-band{left:0;top:1318px;width:1200px;height:342px;background:var(--blue)}
.types-h{left:0;top:1375px;width:1200px;text-align:center;color:var(--white);font-weight:700;font-size:40px;line-height:48px}
.type-card{position:absolute;top:1509px;width:241px}
.type-card .img{height:194px}
.type-card .label{height:51px;background:var(--red);color:var(--white);font-weight:600;font-size:17px;display:flex;align-items:center;justify-content:center}

/* cost */
.cost-bg{left:0;top:1835px;width:1200px;height:593px;background:var(--grey-band)}
.cost-red{left:0;top:1835px;width:497px;height:593px;background:var(--red)}
.cost-photo{left:75px;top:1919px;width:599px;height:426px;background:
  radial-gradient(ellipse 150px 180px at 60% 35%,#d9a98a 0%,rgba(217,169,138,0) 75%),
  radial-gradient(ellipse 160px 120px at 70% 78%,#e46a2a 0%,rgba(228,106,42,0) 75%),
  radial-gradient(ellipse 200px 260px at 12% 60%,#2b2b2b 0%,rgba(43,43,43,0) 80%),
  linear-gradient(120deg,#5b4a3d,#a98d73 50%,#3b4252)}
.cost-h{left:704px;top:1985px;width:440px;font-weight:700;font-size:38px;line-height:51px}

/* testimonials */
.says-h{left:0;top:2490px;width:1200px;text-align:center;font-weight:700;font-size:38px}
.testi{position:absolute;top:2574px;width:512px}
.testi .img{height:345px;position:relative}
.testi .play{position:absolute;left:0;bottom:0;width:90px;height:91px;background:var(--blue);display:flex;align-items:center;justify-content:center}
.testi .quote{margin-top:28px;font-style:italic;font-size:19.5px;line-height:32px}
.testi .name{margin-top:12px;color:var(--red);font-weight:700;font-size:18px}

/* contact band */
.cta-blue{left:0;top:3191px;width:602px;height:222px;background:var(--blue)}
.cta-red{left:602px;top:3191px;width:598px;height:222px;background:var(--red)}
.cta-or{left:574px;top:3276px;width:54px;height:52px;border-radius:10px;background:var(--white);color:var(--blue);font-weight:700;font-size:18px;display:flex;align-items:center;justify-content:center}
.cta-label{color:var(--white);font-weight:600;font-size:19px}
.cta-value{color:var(--white);font-weight:700}

/* footer */
.footer{left:0;top:3413px;width:1200px;height:370px;background:var(--footer);color:var(--white)}
.f-brand{left:75px;top:3484px;width:230px;text-align:center;color:var(--white)}
.f-mark{width:90px;height:90px;border-radius:50%;background:var(--white);margin:0 auto 24px}
.f-name{font-weight:500;font-size:20px;letter-spacing:8px;line-height:26px}
.f-copy{left:75px;top:3664px;font-size:13px;line-height:24px;color:var(--white)}
.f-h{font-weight:600;font-size:16px;letter-spacing:.5px}
.f-links{left:364px;top:3484px;color:var(--white)}
.f-links a{display:block;color:var(--white);text-decoration:none;font-size:15px;line-height:37px}
.f-contact{left:560px;top:3484px;font-size:15px;color:var(--white)}
.f-contact .row{display:flex;gap:14px;margin-top:12px;line-height:26px}
.f-contact svg{flex:none;margin-top:5px}
.f-news{left:884px;top:3484px;width:243px;color:var(--white)}
.f-input{margin-top:14px;height:45px;background:var(--white);color:#555;font-size:13px;display:flex;align-items:center;padding-left:16px}
.f-sub{margin-top:13px;height:46px;background:#111;display:flex;align-items:center;justify-content:center;font-weight:600;font-size:14px}
.f-social{display:flex;gap:22px;margin-top:16px}
.f-social span{width:24px;height:24px;border:2px solid var(--white);border-radius:50%}
</style>
</head>
<body>

<!-- header -->
<div class="abs topbar">
  <span><svg width="22" height="22" viewBox="0 0 24 24" fill="#fff"><path d="M6.6 10.8c1.4 2.8 3.8 5.1 6.6 6.6l2.2-2.2c.3-.3.7-.4 1-.2 1.1.4 2.3.6 3.6.6.6 0 1 .4 1 1V20c0 .6-.4 1-1 1C10.6 21 3 13.4 3 4c0-.6.4-1 1-1h3.5c.6 0 1 .4 1 1 0 1.3.2 2.5.6 3.6.1.3 0 .7-.2 1z"/></svg>+188-888-8888</span>
  <span><svg width="22" height="18" viewBox="0 0 24 18" fill="#fff"><path d="M0 2l12 8 12-8V0H0z"/><path d="M0 5v13h24V5l-12 8z"/></svg>info@companyname.com</span>
</div>
<div class="abs brand"><span class="brand-mark"></span><span class="brand-name">RIDGELINE<br>INSURANCE</span></div>
<nav class="nav">
  <a style="left:313px">HOME</a>
  <a style="left:397px">ABOUT US</a>
  <a style="left:513px">SERVICES</a>
  <a style="left:624px">BLOG</a>
  <a style="left:704px">RESOURCES</a>
  <a style="left:833px">CONTACT US</a>
</nav>
<div class="btn btn-blue" style="left:946px;top:72px;width:181px;height:35px">Request a Quote</div>
<div class="abs header-line"></div>

<!-- hero -->
<div class="abs hero" role="img" aria-label="Blue semi truck driving at speed on a highway at sunset"></div>
<h1 class="abs hero-title">RIDGELINE INSURANCE</h1>
<p class="abs hero-sub">Trucking Insurance Company<br>in California.</p>
<div class="btn btn-red" style="left:946px;top:480px;width:181px;height:34px">Request a Quote</div>

<!-- welcome -->
<h2 class="abs welcome-h">WELCOME TO<br><span class="blue">RIDGELINE INSURANCE</span></h2>
<p class="abs welcome-p">Sed ut perspiciatis unde omnis iste natus error sit voluptatem accusantium doloremque laudantium, totam rem aperiam, eaque ipsa quae ab illo inventore veritatis et quasi architecto beatae vitae dicta sunt explicabo. Nemo enim ipsam voluptatem quia voluptas sit aspernatur aut odit aut fugit, sed quia consequuntur magni dolores eos qui ratione volupta<br>tem sequi nesciunt.</p>
<div class="btn btn-red" style="left:75px;top:1175px;width:165px;height:53px">Read More</div>
<div class="abs welcome-accent"></div>
<div class="abs welcome-photo" role="img" aria-label="Hand sheltering a small model truck on a desk"></div>

<!-- truck types -->
<div class="abs types-band"></div>
<h2 class="abs types-h">TYPES OF COMMERCIAL TRUCK,<br>TRAILERS WE CAN INSURE</h2>
<div class="type-card" style="left:75px"><div class="img" role="img" aria-label="Tanker truck on a highway" style="background:radial-gradient(ellipse 90px 40px at 40% 62%,#e8e8e8 0%,rgba(232,232,232,0) 80%),linear-gradient(180deg,#c9d3dc 0%,#b8c0c6 50%,#7d8487 72%,#5f8a45 88%,#6b6b6b 100%)"></div><div class="label">TANKERS</div></div>
<div class="type-card" style="left:345px"><div class="img" role="img" aria-label="White cargo van in a city street" style="background:radial-gradient(ellipse 80px 40px at 52% 65%,#f2f2f2 0%,rgba(242,242,242,0) 80%),linear-gradient(180deg,#b59c80 0%,#8d7a66 40%,#6c6c6c 70%,#3e3e3e 100%)"></div><div class="label">DRY VAN</div></div>
<div class="type-card" style="left:613px"><div class="img" role="img" aria-label="Blue dump truck" style="background:radial-gradient(ellipse 80px 60px at 30% 55%,#2f4fb0 0%,rgba(47,79,176,0) 80%),radial-gradient(ellipse 70px 60px at 75% 45%,#a8a8a8 0%,rgba(168,168,168,0) 80%),linear-gradient(180deg,#dfe6ee 0%,#b7c0cc 45%,#707070 100%)"></div><div class="label">DUMP TRUCKS</div></div>
<div class="type-card" style="left:886px"><div class="img" role="img" aria-label="Red truck hauling a flatbed trailer" style="background:radial-gradient(ellipse 70px 50px at 38% 55%,#c0272d 0%,rgba(192,39,45,0) 80%),linear-gradient(180deg,#e6ecef 0%,#7f9a6a 35%,#9a9a8e 65%,#7a7a6e 100%)"></div><div class="label">FLATBED</div></div>

<!-- cost -->
<div class="abs cost-bg"></div>
<div class="abs cost-red"></div>
<div class="abs cost-photo" role="img" aria-label="Smiling truck driver giving a thumbs up from the cab"></div>
<h2 class="abs cost-h">HOW MUCH DOES CALIFORNIA COMMERCIAL TRUCK INSURANCE COST?</h2>
<div class="btn btn-blue" style="left:704px;top:2229px;width:180px;height:35px">Request a Quote</div>

<!-- testimonials -->
<h2 class="abs says-h">WHAT OUR CUSTOMER SAYS</h2>
<div class="testi" style="left:75px">
  <div class="img" role="img" aria-label="Customer in a red vest standing in front of trucks" style="background:radial-gradient(ellipse 90px 130px at 68% 72%,#c8242b 0%,rgba(200,36,43,0) 80%),radial-gradient(ellipse 160px 140px at 20% 30%,#2e4f9c 0%,rgba(46,79,156,0) 80%),linear-gradient(180deg,#7a8496 0%,#8d8f94 60%,#6d6d6d 100%)">
    <div class="play"><svg width="56" height="56" viewBox="0 0 56 56"><circle cx="28" cy="28" r="24" fill="none" stroke="#fff" stroke-width="4"/><path d="M22 17v22l18-11z" fill="#fff"/></svg></div>
  </div>
  <p class="quote">“ Sed ut perspiciatis unde omnis iste natus error sit voluptatem accusantium doloremque laudantium, totam rem aperiam, eaque ipsa quae ab illo inventore..”</p>
  <p class="name">-NAME HEADING</p>
</div>
<div class="testi" style="left:615px">
  <div class="img" role="img" aria-label="Customer with arms crossed in front of a truck trailer" style="background:radial-gradient(ellipse 110px 150px at 38% 70%,#2a3246 0%,rgba(42,50,70,0) 80%),radial-gradient(ellipse 130px 120px at 82% 35%,#c9963f 0%,rgba(201,150,63,0) 80%),linear-gradient(180deg,#d8d8d8 0%,#b9b4ab 55%,#6e6a66 100%)">
    <div class="play"><svg width="56" height="56" viewBox="0 0 56 56"><circle cx="28" cy="28" r="24" fill="none" stroke="#fff" stroke-width="4"/><path d="M22 17v22l18-11z" fill="#fff"/></svg></div>
  </div>
  <p class="quote">“ Sed ut perspiciatis unde omnis iste natus error sit voluptatem accusantium doloremque laudantium, totam rem aperiam, eaque ipsa quae ab illo inventore..”</p>
  <p class="name">-NAME HEADING</p>
</div>

<!-- contact band -->
<div class="abs cta-blue"></div>
<div class="abs cta-red"></div>
<svg class="abs" style="left:75px;top:3265px" width="76" height="70" viewBox="0 0 76 70" fill="none" stroke="#fff" stroke-width="3"><path d="M12 50c-6-2-8-8-8-16S10 8 30 8s26 14 26 24"/><rect x="4" y="30" width="10" height="18" rx="3"/><rect x="48" y="30" width="10" height="18" rx="3"/><path d="M53 48c0 10-8 14-18 14"/><rect x="54" y="2" width="20" height="14" rx="2"/></svg>
<p class="abs cta-label" style="left:175px;top:3264px">EXPERTS AVAILABLE CALL</p>
<p class="abs cta-value" style="left:175px;top:3290px;font-size:44px;line-height:56px">+188-888-8888</p>
<div class="abs cta-or">OR</div>
<svg class="abs" style="left:668px;top:3265px" width="64" height="70" viewBox="0 0 64 70" fill="none" stroke="#fff" stroke-width="3"><path d="M2 28l30-22 30 22v38H2z"/><path d="M2 28l30 22 30-22"/><path d="M2 66l22-20M62 66L40 46"/><circle cx="32" cy="26" r="8"/></svg>
<p class="abs cta-label" style="left:749px;top:3268px">EMAIL US FOR QUOTES</p>
<p class="abs cta-value" style="left:749px;top:3296px;font-size:28px">info@Ridgeline Insurance</p>

<!-- footer -->
<footer class="abs footer"></footer>
<div class="abs f-brand"><div class="f-mark"></div><p class="f-name">RIDGELINE<br>INSURANCE</p></div>
<p class="abs f-copy">Copyright © 2023 Company Name<br>All Rights Reserved</p>
<div class="abs f-links">
  <p class="f-h" style="margin-bottom:4px">QUICK LINKS</p>
  <a>Home</a><a>About Us</a><a>Services</a><a>Blog</a><a>Resources</a><a>Contact Us</a>
</div>
<div class="abs f-contact">
  <p class="f-h">CONTACT INFO</p>
  <div class="row"><svg width="18" height="16" viewBox="0 0 18 16" fill="#fff"><path d="M0 2l6-2 6 2 6-2v14l-6 2-6-2-6 2z"/></svg><span>Nemo enim ipsam vcons<br>luptatem quia</span></div>
  <div class="row"><svg width="16" height="16" viewBox="0 0 24 24" fill="#fff"><path d="M6.6 10.8c1.4 2.8 3.8 5.1 6.6 6.6l2.2-2.2c.3-.3.7-.4 1-.2 1.1.4 2.3.6 3.6.6.6 0 1 .4 1 1V20c0 .6-.4 1-1 1C10.6 21 3 13.4 3 4c0-.6.4-1 1-1h3.5c.6 0 1 .4 1 1 0 1.3.2 2.5.6 3.6.1.3 0 .7-.2 1z"/></svg><span>+188-888-8888</span></div>
  <div class="row"><svg width="16" height="13" viewBox="0 0 24 18" fill="#fff"><path d="M0 2l12 8 12-8V0H0z"/><path d="M0 5v13h24V5l-12 8z"/></svg><span>info@companyname.com</span></div>
</div>
<div class="abs f-news">
  <p class="f-h">NEWSLETTER SIGN UP</p>
  <div class="f-input">Email Address</div>
  <div class="f-sub">SUBSCRIBE</div>
  <p class="f-h" style="margin-top:26px">CONNECT US</p>
  <div class="f-social"><span></span><span></span><span></span><span></span><span></span></div>
</div>

</body>
</html>
```